I need a packaging design for a Buttery Popcorn Spray in can.

The brand name is Kernel Kingdom-The flavor is Golden Gush(main competitor design attached)

The die line is uploaded.

We want it be a fun, catchy design that includes popcorn on the design reminds people of going to the movies... some nastalgia is good. Open to colors. But we are open.

Company name is Kernel Kingdom. Flavor is Golden Gush -both need to be present.

Final design should communicate enjoyment, relaxation, delicious flavor.

Target Market(s)

People who like to eat popcorn at home.

Industry/Entity Type

Food

Requirements
Must have
• Popcorn, movie theater setting

```html
<!DOCTYPE html>
<html lang="en">
<head>
<meta charset="utf-8">
<title>Kernel Kingdom – Golden Gush Buttery Popcorn Spray</title>
<link rel="stylesheet" href="https://fonts.googleapis.com/css2?family=Luckiest+Guy&family=Archivo+Black&display=swap">
<style>
  :root {
    --backdrop: #f5cd6c;
    --label-red: #e8232e;
    --label-deep-red: #c9141f;
    --label-yellow: #fcd22e;
    --stripe-pink: #f0609e;
    --stripe-aqua: #6fd3d6;
    --stripe-orange: #f99a3a;
    --title-white: #ffffff;
    --ink: #2a2a2a;
    --popcorn-gold: #f7c531;
    --popcorn-cream: #fdf0b4;
  }
  * { margin: 0; padding: 0; box-sizing: border-box; }
  html, body { width: 1200px; height: 1200px; overflow: hidden; }
  body {
    background: var(--backdrop);
    display: flex;
    align-items: center;
    justify-content: center;
  }
  .can-label {
    position: relative;
    width: 640px;
    height: 1040px;
    overflow: hidden;
    border-radius: 6px;
    background: var(--label-red);
  }
  .rainbow-bands {
    position: absolute;
    inset: 0;
    width: 100%;
    height: 100%;
  }
  .brand-line {
    position: absolute;
    top: 70px;
    left: 60px;
    font-family: "Archivo Black", sans-serif;
    font-size: 24px;
    line-height: 1.15;
    color: var(--title-white);
    letter-spacing: 1px;
  }
  .brand-line::before {
    content: "";
    display: inline-block;
    width: 14px;
    height: 14px;
    border-radius: 50%;
    background: var(--label-yellow);
    margin-right: 10px;
    vertical-align: 2px;
  }
  .product-title {
    position: absolute;
    top: 160px;
    left: 0;
    width: 100%;
    text-align: center;
    font-family: "Luckiest Guy", sans-serif;
    font-size: 200px;
    font-weight: 400;
    line-height: 1;
    color: var(--title-white);
    -webkit-text-stroke: 6px var(--ink);
    paint-order: stroke fill;
    text-shadow: 0 10px 0 var(--ink);
    transform: rotate(-4deg);
  }
  .bucket-illustration {
    position: absolute;
    top: 430px;
    left: 50px;
    width: 540px;
    height: 560px;
    border-radius: 48% 48% 14px 14px / 28% 28% 14px 14px;
    background: linear-gradient(180deg,
      var(--popcorn-cream) 0%,
      var(--popcorn-gold) 38%,
      var(--stripe-orange) 62%,
      var(--label-red) 100%);
  }
  .flavor-badge {
    position: absolute;
    left: 50%;
    bottom: 70px;
    padding: 10px 18px;
    background: var(--label-yellow);
    border: 3px solid var(--label-deep-red);
    border-radius: 6px;
    text-align: center;
    white-space: nowrap;
    font-family: "Archivo Black", sans-serif;
    color: var(--label-deep-red);
    transform: translateX(-50%) rotate(-3deg);
  }
  .flavor-badge .badge-small { font-size: 15px; letter-spacing: 1px; }
  .flavor-badge .badge-large { font-size: 28px; line-height: 1.1; }
</style>
</head>
<body>
  <main class="can-label">
    <svg class="rainbow-bands" viewBox="0 0 640 1040" preserveAspectRatio="none" aria-hidden="true">
      <polygon points="0,560 640,260 640,340 0,640" fill="var(--stripe-pink)"/>
      <polygon points="0,640 640,340 640,420 0,720" fill="var(--stripe-aqua)"/>
      <polygon points="0,720 640,420 640,500 0,800" fill="var(--stripe-orange)"/>
      <polygon points="0,800 640,500 640,1040 0,1040" fill="var(--label-yellow)"/>
    </svg>

    <p class="brand-line">KERNEL<br>KINGDOM</p>

    <h1 class="product-title">POP!</h1>

    <div class="bucket-illustration" role="img" aria-label="Cartoon movie theater popcorn bucket with red and white stripes, overflowing with fluffy buttery popcorn, loose kernels flying around it"></div>

    <div class="flavor-badge">
      <div class="badge-small">GOLDEN GUSH</div>
      <div class="badge-large">BUTTERY SPRAY</div>
    </div>
  </main>
</body>
</html>
```